2 Flow Charts showing Fair Trade vs Market Trade****See new image*****

I am starting a coffee roasting company where I warehouse coffee for farmers I met in Nicaragua as a Unity Service Brigade Volunteer.

I need one flow chart to show the normal path of coffee, from the producer to the exporter, to the importer, to the roaster, and ultimately to the consumer, each of which taking a little along the way, leaving the farmer less.

Then another flow chart showing a close relationship between my company (Lark Hollow Coffee) and the producer, with out the exporter/importer, and more money going to the farmer.

I have included my attempt at the flow charts, which look clunky and are in super low res.

You can see how I want to use the flow charts in the following website:

larkhollowbeanworks.com

****** Just reduced the verbiage on the Flow Charts****************
***************See new image*******************************

Target Market(s)

Coffee consumers interested in fair trade.

Industry/Entity Type

It Company

Font styles to use
Sans Serif

Requirements
Must have
• Originally thinking black and white, but am open to color.
Nice to have
• Would like to see a design in both color and monochrome. I am having a difficult time determining which would look better on the site.

```html
<!DOCTYPE html>
<html lang="en">
<head>
<meta charset="utf-8">
<title>Lark Hollow Trade</title>
<link rel="stylesheet" href="https://fonts.googleapis.com/css2?family=Fira+Sans:wght@400;600;800&display=swap">
<style>
  :root {
    --blue: #3a86c8;
    --orange: #ff4a22;
    --pink: #f9c9bd;
    --bean: #8a5a4e;
    --paper: #ffffff;
  }
  html, body { margin: 0; padding: 0; overflow: hidden; background: var(--paper); }
  .canvas {
    position: relative; width: 1200px; height: 1000px; overflow: hidden;
    background: var(--paper); font-family: "Fira Sans", sans-serif; color: var(--blue);
  }
  .flow { position: absolute; left: 0; top: 0; }
  .title {
    position: absolute; left: 0; top: 78px; width: 1200px; margin: 0;
    text-align: center; font-size: 62px; font-weight: 800; letter-spacing: 0.5px; line-height: 1;
  }
  .node-label {
    position: absolute; margin: 0; font-size: 21px; font-weight: 800; line-height: 1;
  }
  .node-label--producer { left: 108px; top: 377px; }
  .node-label--roaster { left: 98px; top: 689px; }
  .note {
    position: absolute; margin: 0; font-size: 19px; line-height: 26px; font-weight: 400;
  }
  .note strong { font-weight: 600; }
  .note--export { left: 262px; top: 262px; width: 360px; }
  .note--support { left: 262px; top: 564px; width: 300px; }
  .note--coffee { left: 746px; top: 546px; width: 450px; font-size: 18.5px; }
  .coffee-heading {
    position: absolute; left: 746px; top: 507px; margin: 0;
    font-size: 29px; font-weight: 800; color: var(--orange); line-height: 1;
  }
  .money {
    position: absolute; margin: 0; font-size: 46px; font-weight: 800; line-height: 1;
  }
  .money--top { left: 570px; top: 402px; }
  .money--bottom { left: 570px; top: 714px; }
  .money-small {
    position: absolute; left: 44px; top: 372px; margin: 0;
    font-size: 21px; font-weight: 800; color: var(--pink); line-height: 1;
  }
  .figure-producer {
    position: absolute; left: 134px; top: 262px; width: 66px; height: 104px;
    border-radius: 30px 30px 10px 10px; background: var(--blue); opacity: 0.85;
  }
  .figure-cup {
    position: absolute; left: 804px; top: 372px; width: 120px; height: 118px;
    border-radius: 10px 10px 40px 40px; background: var(--blue); opacity: 0.85;
  }
</style>
</head>
<body>
<main class="canvas">
  <h1 class="title">LARK HOLLOW TRADE</h1>

  <svg class="flow" width="1200" height="1000" viewBox="0 0 1200 1000" aria-hidden="true">
    <!-- support loop -->
    <polyline points="40,383 10,383 10,700 42,700" fill="none" stroke="var(--pink)" stroke-width="4"/>
    <line x1="66" y1="383" x2="88" y2="383" stroke="var(--pink)" stroke-width="4"/>
    <polygon points="96,383 84,376 84,390" fill="var(--pink)"/>

    <!-- left bracket -->
    <polyline points="150,423 42,423 42,690" fill="none" stroke="var(--blue)" stroke-width="4"/>
    <polyline points="42,714 42,738 150,738" fill="none" stroke="var(--blue)" stroke-width="4"/>

    <!-- revenue loop -->
    <polyline points="637,423 698,423 698,738 637,738" fill="none" stroke="var(--blue)" stroke-width="4"/>
    <line x1="222" y1="423" x2="565" y2="423" stroke="var(--blue)" stroke-width="4"/>
    <polygon points="207,423 224,413 224,433" fill="var(--blue)"/>
    <line x1="222" y1="738" x2="565" y2="738" stroke="var(--blue)" stroke-width="4"/>
    <polygon points="207,738 224,728 224,748" fill="var(--blue)"/>

    <!-- step markers -->
    <circle cx="167" cy="425" r="16" fill="var(--paper)" stroke="var(--orange)" stroke-width="3.5"/>
    <text x="167" y="432" text-anchor="middle" font-family="Fira Sans, sans-serif" font-weight="800" font-size="19" fill="var(--blue)">1</text>
    <circle cx="167" cy="738" r="16" fill="var(--paper)" stroke="var(--orange)" stroke-width="3.5"/>
    <text x="167" y="745" text-anchor="middle" font-family="Fira Sans, sans-serif" font-weight="800" font-size="19" fill="var(--blue)">1</text>
    <circle cx="698" cy="577" r="17" fill="var(--orange)" stroke="var(--blue)" stroke-width="4"/>
    <text x="698" y="584" text-anchor="middle" font-family="Fira Sans, sans-serif" font-weight="800" font-size="19" fill="var(--paper)">2</text>

    <!-- bean handoff -->
    <line x1="167" y1="465" x2="167" y2="482" stroke="var(--orange)" stroke-width="4"/>
    <line x1="167" y1="518" x2="167" y2="530" stroke="var(--orange)" stroke-width="4"/>
    <polygon points="167,542 159,530 175,530" fill="var(--orange)"/>
    <ellipse cx="167" cy="500" rx="7" ry="10" fill="var(--bean)" role="img" aria-label="Coffee bean"/>

    <!-- roaster house -->
    <g class="house">
      <polygon points="167,565 110,615 224,615" fill="var(--orange)"/>
      <rect x="124" y="612" width="86" height="60" fill="var(--orange)"/>
      <rect x="157" y="645" width="21" height="27" fill="var(--paper)"/>
    </g>
  </svg>

  <div class="figure-producer" role="img" aria-label="Icon of a coffee farmer in a hat"></div>
  <p class="money-small">$</p>
  <p class="node-label node-label--producer">PRODUCER</p>
  <p class="node-label node-label--roaster">LARK HOLLOW</p>

  <p class="note note--export"><strong>LARK HOLLOW facilitates the export and import of the coffee</strong>, and holds that coffee on the farmers behalf until it is ready to be sold in a value added form</p>
  <p class="note note--support">Only a small monetary exchange occurs initially. This small sum <strong>is provided to the producer as support</strong> until additional revenue occurs</p>

  <p class="money money--top">$$</p>
  <p class="money money--bottom">$$</p>

  <div class="figure-cup" role="img" aria-label="Icon of a steaming coffee cup with a bean"></div>
  <h2 class="coffee-heading">YOUR COFFEE</h2>
  <p class="note note--coffee">As the coffee is roasted and sold, the revenues are split between <strong>LARK HOLLOW and the producers.</strong> The producers benefit from higher coffee prices not subject to market conditions, and LARK HOLLOW benefits from <strong>decreased upfront costs</strong> and more direct farmer to consumer experience!</p>
</main>
</body>
</html>
```